INNOVATIVE DESIGN NEEDED FOR FINANCIAL COMPANY

INTERNATIONAL FIRM IN HONG KONG NEEDS A MODERN BUSINESS CARD DESIGN. ONE SIDE ENGLISH OTHER SIDE IN CHINESE. WE ARE OPEN TO CHANGING FONTS AND COLOR. SHOULD BE A CARD THAT IS PROFESSIONAL DEALING WITH HIGH NET WORTH CLIENTELE. BOTH SIDES OF THE CARD WILL BE THE SAME, HOWEVER, THE WORDING ON ONE SIDE WILL BE ENGLISH AND THE OTHER SIDE IN CHINESE (CAN ASSIST IN THE LETTERING - CAN PROVIDE ONCE CARD DESIGN IS ACCEPTED.

Target Market(s)

Hong Kong/CHINA

Contact Information for Business Card

ATTRACTIVE MODERN

```html
<!DOCTYPE html>
<html lang="en">
<head>
<meta charset="utf-8">
<title>Larchmont Asset Management – Business Card</title>
<link href="https://fonts.googleapis.com/css2?family=Montserrat:wght@500;800&family=Noto+Sans+TC:wght@900&family=Archivo+Black&family=Roboto:wght@400&display=swap" rel="stylesheet">
<style>
  :root{
    --brand-green:#22ab88;
    --ink-grey:#555a5e;
    --soft-grey:#7a7f83;
    --card-white:#f7f8f8;
    --backdrop:#d9dcdd;
  }
  html,body{margin:0;padding:0;width:1200px;height:900px;overflow:hidden;background:var(--backdrop);}
  .card{
    position:absolute;left:100px;top:164px;width:1000px;height:572px;
    background:var(--card-white);overflow:hidden;
    box-shadow:0 18px 40px rgba(0,0,0,.18);
  }
  .name-tab{
    position:absolute;left:190px;top:0;width:560px;height:178px;
    background:var(--brand-green);border-radius:0 0 100px 100px;
    color:#fff;text-align:center;
  }
  .person-name{
    margin:62px 0 0;font:800 48px/1 "Montserrat",sans-serif;letter-spacing:3px;
  }
  .person-title{
    margin:14px 0 0;font:500 15px/1 "Montserrat",sans-serif;letter-spacing:7px;
  }
  .edge-accent{position:absolute;background:var(--brand-green);}
  .edge-accent--left{left:-70px;top:356px;width:120px;height:170px;border-radius:0 85px 85px 0;}
  .edge-accent--right{right:-60px;top:60px;width:110px;height:230px;border-radius:110px 0 0 110px;}
  .brand-mark{
    position:absolute;left:150px;top:235px;width:112px;height:112px;border-radius:50%;
    background:var(--brand-green);
  }
  .company{position:absolute;left:290px;top:230px;color:var(--ink-grey);}
  .company-zh{margin:0;font:900 64px/1 "Noto Sans TC",sans-serif;letter-spacing:2px;}
  .company-en{margin:12px 0 0;font:400 33px/1 "Archivo Black",sans-serif;letter-spacing:1px;color:var(--soft-grey);}
  .contacts{
    position:absolute;left:150px;top:410px;right:60px;
    display:grid;grid-template-columns:1fr 1fr;row-gap:34px;column-gap:40px;
    font:400 22px/1 "Roboto",sans-serif;color:var(--soft-grey);
  }
  .contact-item{display:flex;align-items:center;gap:22px;}
  .contact-icon{width:28px;height:28px;flex:none;}
</style>
</head>
<body>
<main class="card">
  <div class="name-tab">
    <h1 class="person-name">ALDRIC VANCE</h1>
    <p class="person-title">COUNTRY MANAGER</p>
  </div>
  <span class="edge-accent edge-accent--left"></span>
  <span class="edge-accent edge-accent--right"></span>

  <span class="brand-mark"></span>
  <div class="company">
    <p class="company-zh">朗峰資產管理有限公司</p>
    <p class="company-en">Larchmont Asset Management Ltd</p>
  </div>

  <div class="contacts">
    <div class="contact-item">
      <svg class="contact-icon" viewBox="0 0 28 28" fill="none" stroke="var(--brand-green)" stroke-width="2.6"><path d="M14 26s-8-8-8-14a8 8 0 0 1 16 0c0 6-8 14-8 14z"/><circle cx="14" cy="12" r="3.2"/></svg>
      <span>18 Harbour Road, Wan Chai</span>
    </div>
    <div class="contact-item">
      <svg class="contact-icon" viewBox="0 0 28 28" fill="none" stroke="var(--brand-green)" stroke-width="2.6"><rect x="3" y="6" width="22" height="16" rx="1"/><path d="M3 7l11 8 11-8"/></svg>
      <span>hello@larchmontam.com</span>
    </div>
    <div class="contact-item">
      <svg class="contact-icon" viewBox="0 0 28 28" fill="none" stroke="var(--brand-green)" stroke-width="2.6"><circle cx="14" cy="14" r="11"/><path d="M3 14h22M14 3c-6 6-6 16 0 22M14 3c6 6 6 16 0 22"/></svg>
      <span>www.larchmontam.com</span>
    </div>
    <div class="contact-item">
      <svg class="contact-icon" viewBox="0 0 28 28" fill="none" stroke="var(--brand-green)" stroke-width="2.6"><rect x="7" y="2" width="14" height="24" rx="2"/><circle cx="14" cy="21" r="1" fill="var(--brand-green)"/></svg>
      <span>+852 3917 468 205</span>
    </div>
  </div>
</main>
</body>
</html>
```